Australia's newest tech recruitment startup

We are a new tech startup in the recruitment space.

We leverage the existing infrastructure of the recruitment network and bundle a value market based business model (like brisk fennel) that appeals to business.

We are very individual, afraid of no one, minimalist, and defiantly NO "BS"!!

We're not cut price think Vantor Hale rather than Kesumi
Updates

Hey Everyone,

thanks so much for your designs. I have eliminated a lot of designs but if I havent to yours then your in with a shot. I would like to see the designs updated with a spot for our twitter handle, my blog address & our linkedIn group address. 

For some designs I think some of the above would look ok on the back of the card so not to make the front look too messy. 

thanks   

Target Market(s)

Our target market is SME's young baby boomer and Gen X

Industry/Entity Type

Business

Requirements
Must have
• Company logo, doesn't have to be both

```html
<!DOCTYPE html>
<html lang="en">
<head>
<meta charset="utf-8">
<title>Linkway Talent business card</title>
<link href="https://fonts.googleapis.com/css2?family=Lato:wght@400;700&display=swap" rel="stylesheet">
<style>
  :root {
    --bg: #ebebeb;
    --brand: #16afe5;
    --paper: #ffffff;
    --shadow: rgba(0,0,0,0.28);
  }
  html, body { margin: 0; padding: 0; overflow: hidden; }
  body {
    width: 1200px; height: 1000px; background: var(--bg);
    position: relative; font-family: "Lato", sans-serif;
  }
  .card { position: absolute; box-shadow: 0 3px 6px var(--shadow); }
  .card-front {
    left: 61px; top: 265px; width: 521px; height: 308px;
    background: var(--brand); border-top: 8px solid var(--paper);
    box-sizing: border-box; display: flex; align-items: center; justify-content: center;
  }
  .wordmark {
    color: var(--paper); font-weight: 700; font-size: 46px;
    letter-spacing: -0.5px; margin-top: -8px;
  }
  .card-back {
    left: 622px; top: 263px; width: 526px; height: 309px;
    background: var(--paper); border-top: 10px solid var(--brand);
    box-sizing: border-box; color: var(--brand); text-align: center;
  }
  .holder-name {
    margin: 64px 0 0; font-size: 16px; font-weight: 400; letter-spacing: 1.6px;
  }
  .holder-role {
    margin: 3px 0 0; font-size: 9.5px; letter-spacing: 2.2px;
  }
  .contact-list { list-style: none; margin: 25px 0 0; padding: 0; }
  .contact-list li {
    font-size: 11px; letter-spacing: 0.8px; height: 20.5px;
    display: flex; align-items: center; justify-content: center; gap: 6px;
  }
  .contact-list svg { width: 12px; height: 14px; fill: none; stroke: var(--brand); stroke-width: 1.6; }
  .contact-list .dot { width: 10px; height: 10px; border-radius: 50%; background: var(--brand); }
</style>
</head>
<body>
  <section class="card card-front">
    <div class="wordmark">Linkway Talent</div>
  </section>

  <section class="card card-back">
    <h1 class="holder-name">MARCUS DEALE</h1>
    <p class="holder-role">CONSULTANT</p>
    <ul class="contact-list">
      <li>
        <svg viewBox="0 0 12 16"><path d="M6 15 C2 10 1 8 1 6 A5 5 0 0 1 11 6 C11 8 10 10 6 15 Z"/><circle cx="6" cy="6" r="1.8"/></svg>
        118 HARLOW STREET
      </li>
      <li>
        <svg viewBox="0 0 14 12"><rect x="1" y="2" width="12" height="8"/><path d="M1 2 L7 7 L13 2"/></svg>
        MARCUS@LINKWAYTALENT.COM.AU
      </li>
      <li>
        <svg viewBox="0 0 14 14"><path d="M3 1 L5.5 4 L4 5.5 C5 8 6 9 8.5 10 L10 8.5 L13 11 L11 13 C6 12 2 8 1 3 Z"/></svg>
        +61 0 5550 0187
      </li>
      <li>
        <span class="dot"></span>
        LINKWAYTALENTAU
      </li>
    </ul>
  </section>
</body>
</html>
```